vel nova
Zielgruppe
My service company has specialists in Sales, Marketing and Change Management. Our target group is the 1st and 2nd management level of enterprises, who want to align their strategy at new market situations or to change their distribution, communication or product concept.
We help our clients in defined time frames or projects not only in defining new strategies and concepts but also in implementation and measurements of the results.
Aufgabenstellung
I'm looking for a design of business cards and A4 letter paper. The company name is "vel nova"; my name ist Viktor Nolt...
So the name of my company stands for Management on time (vel nova) and vn stands for my name (initials)
Logo see enclosed.

```html
<!DOCTYPE html>
<html lang="de">
<head>
<meta charset="utf-8">
<title>vel nova – Briefbogen</title>
<link href="https://fonts.googleapis.com/css2?family=Arimo:wght@400&display=swap" rel="stylesheet">
<style>
  :root {
    --backdrop: #ffffff;
    --paper: #fbfbf8;
    --ink: #111111;
    --brand-navy: #1f2b57;
    --footer-grey: #6b6b6b;
    --rule: #777777;
  }
  * { margin: 0; padding: 0; box-sizing: border-box; }
  html, body {
    width: 1200px; height: 1200px; overflow: hidden;
    background: var(--backdrop);
    font-family: "Arimo", Arial, sans-serif;
    color: var(--ink);
  }
  .letterhead {
    position: absolute; left: 174px; top: 28px;
    width: 807px; height: 1140px;
    background: var(--paper);
  }
  .brand-name {
    position: absolute; right: 35px; top: 106px;
    font-size: 34px; color: var(--brand-navy); letter-spacing: 0.5px;
  }
  .block { position: absolute; left: 116px; font-size: 11px; line-height: 12.5px; }
  .sender-line { top: 153px; }
  .recipient { top: 172px; }
  .letter-body {
    position: absolute; left: 116px; top: 360px; width: 580px;
    font-size: 12.2px; line-height: 17.1px;
  }
  .letter-body p { margin-bottom: 17.1px; }
  .closing { position: absolute; left: 116px; top: 819px; font-size: 12.2px; }
  .signature { position: absolute; left: 115px; top: 937px; font-size: 13.5px; line-height: 15.5px; }
  .footer-rule {
    position: absolute; left: 38px; top: 1045px; width: 731px;
    border-top: 1px solid var(--rule);
  }
  .footer {
    position: absolute; left: 0; top: 1063px; width: 808px;
    text-align: center; font-size: 10.4px; line-height: 19.5px;
    color: var(--footer-grey);
  }
  .footer span { margin: 0 4px; }
</style>
</head>
<body>
<main class="letterhead">
  <div class="brand-name">vel nova</div>

  <div class="block sender-line">Viktor Nolt&nbsp;&nbsp; Adresse 1&nbsp;&nbsp; Adresse 2</div>
  <div class="block recipient">Max Mustermann<br>Straße<br>Ort</div>

  <div class="letter-body">
    <p>Sehr geehrter Herr,</p>
    <p>Esse ut ex. Sed esse mollit quis laboris in pariatur, anim ut aliquip ullamco voluptate. Ex consectetur culpa in eu, proident aliqua mollit sint reprehenderit?</p>
    <p>Incididunt ut in dolore reprehenderit aliqua ad, mollit anim fugiat ea. Enim consequat ad, ipsum ad sint culpa amet consectetur, sed cupidatat. Sit commodo ut. Non, nisi excepteur, fugiat voluptate ullamco eu labore: Pariatur sint laboris. Ipsum ea culpa qui nisi id exercitation, voluptate sit qui esse. Nisi, sunt ipsum occaecat commodo ut, magna veniam sed sit. Nisi officia minim reprehenderit dolore exercitation in fugiat, pariatur do reprehenderit dolore? Dolore, nostrud dolor velit.</p>
    <p>Aute aliqua, sed nostrud ut in ex nulla id ut non mollit aute voluptate. Occaecat anim ea nostrud et dolor est fugiat tempor excepteur. Amet, esse culpa commodo proident ut commodo do aute.<br>Qui sed adipisicing voluptate est. Fugiat sint veniam in duis non deserunt sint commodo: Occaecat dolore magna ea mollit, enim dolor exercitation dolore sunt magna aute lorem ea ad exercitation?</p>
    <p>Consectetur id ea proident. Dolore sunt velit et reprehenderit aliqua eiusmod. Exercitation eu laboris ex occaecat deserunt dolore et excepteur sint in dolore nostrud laboris dolore culpa quis cupidatat. Ea cillum et. In, consectetur amet.</p>
    <p>In elit ullamco culpa, enim reprehenderit est dolore magna, ad lorem. Ipsum ea, minim mollit sit minim. Sed voluptate velit dolor in magna non aliqua cillum in officia in excepteur.Officia veniam ut, pariatur ad veniam reprehenderit ex sint consequat magna. Amet sunt, duis velit do qui culpa, adipisicing sint mollit officia in culpa aliqua. Lorem, aliqua non labore est enim. Ad officia commodo do eu consequat. Sunt in, eu cupidatat, qui aute proident, adipisicing fugiat dolore velit ut in sint eiusmod commodo laboris do.</p>
  </div>

  <div class="closing">Mit freundlichen Grüßen</div>
  <div class="signature">Viktor Nolt<br>Geschäftsführer</div>

  <div class="footer-rule"></div>
  <div class="footer">
    <div>Viktor Nolt&nbsp;&nbsp; Adresse 1&nbsp;&nbsp; Adresse 2</div>
    <div><span>Tel: +49 (0) 000000000</span><span>Fax: +49 (0) 11111</span><span>E-mail: info@xxxx.de</span><span>Web: www.xxxxxxx.de</span></div>
    <div><span>Bankverbindung: xxxxxxxxxx</span><span>IBAN: xxxxxxxxxxxxxx</span><span>BIC: xxxxxxxxxxxxxxxxxx</span></div>
  </div>
</main>
</body>
</html>
```